Business Card Design Project

We need a Business Card for an Mechanical Engineering firm in Singapore. The design should be Modern & Technical looking, yet eye catching.

Our company deals in Cutting Tools & Machine Accessories for the Manufacturing Industries such as Oil & Gas, Aero Space, etc... For more information on our Company, you can either email me or view our website www.valtrion.com.sg.

We are trying to revamp our image to give our consumers a fresh new perspective to our company, so we welcome all ideas.

Industry/Entity Type

Business

Requirements
Must have
• Must incorporate New Company Logo into the card as shown in Uploaded file.

```html
<!DOCTYPE html>
<html lang="en">
<head>
<meta charset="utf-8">
<title>Valtrion Tools – Business Card</title>
<link rel="stylesheet" href="https://fonts.googleapis.com/css2?family=Bodoni+Moda:wght@400;500&family=Oswald:wght@300;400&display=swap">
<style>
  :root {
    --backdrop: #d6d8da;
    --card: #ffffff;
    --ink: #2b2724;
    --brand-red: #ad1f3a;
    --shadow: rgba(0, 0, 0, 0.22);
  }
  html, body {
    margin: 0;
    padding: 0;
    overflow: hidden;
  }
  .canvas {
    position: relative;
    width: 1200px;
    height: 842px;
    background: var(--backdrop);
    overflow: hidden;
  }
  .card-shape {
    position: absolute;
    left: 0;
    top: 0;
    width: 1200px;
    height: 842px;
    filter: drop-shadow(0 10px 18px var(--shadow));
  }
  .card-shape path,
  .card-shape rect,
  .card-shape circle { fill: var(--card); }
  .brand {
    position: absolute;
    left: 178px;
    top: 300px;
    display: flex;
    align-items: center;
    gap: 14px;
  }
  .brand-dot {
    width: 22px;
    height: 22px;
    border-radius: 50%;
    background: var(--brand-red);
  }
  .brand-name {
    font-family: "Oswald", sans-serif;
    font-weight: 400;
    font-size: 44px;
    letter-spacing: 1px;
    color: var(--brand-red);
    line-height: 1;
  }
  .contact {
    position: absolute;
    left: 190px;
    font-family: "Bodoni Moda", serif;
    font-size: 19px;
    line-height: 24px;
    color: var(--ink);
    text-transform: uppercase;
    margin: 0;
  }
  .contact--address { top: 404px; }
  .contact--lines { top: 548px; }
  .person {
    position: absolute;
    left: 410px;
    top: 512px;
  }
  .person-name {
    font-family: "Oswald", sans-serif;
    font-weight: 300;
    font-size: 36px;
    letter-spacing: 1px;
    color: var(--ink);
    margin: 0;
    line-height: 1.1;
  }
  .person-role {
    font-family: "Bodoni Moda", serif;
    font-size: 22px;
    color: var(--brand-red);
    margin: 0;
    text-transform: uppercase;
    line-height: 1.1;
  }
</style>
</head>
<body>
<main class="canvas">
  <svg class="card-shape" viewBox="0 0 1200 842" aria-hidden="true">
    <g class="card-body">
      <rect x="135" y="161" width="650" height="520"/>
      <circle cx="810" cy="421" r="218"/>
      <g class="gear-teeth" transform="translate(810 421)">
        <rect x="-42" y="-255" width="84" height="60" transform="rotate(0)"/>
        <rect x="-42" y="-255" width="84" height="60" transform="rotate(45)"/>
        <rect x="-42" y="-255" width="84" height="60" transform="rotate(90)"/>
        <rect x="-42" y="-255" width="84" height="60" transform="rotate(135)"/>
        <rect x="-42" y="-255" width="84" height="60" transform="rotate(180)"/>
      </g>
    </g>
  </svg>

  <div class="brand">
    <span class="brand-dot"></span>
    <span class="brand-name">VALTRION TOOLS</span>
  </div>

  <p class="contact contact--address">
    Valtrion Tools Pte Ltd<br>
    58 Kestrel Crescent #03-12,<br>
    Meridian Works Hub,<br>
    Singapore 629471
  </p>

  <div class="person">
    <h1 class="person-name">HELENA MARWICK</h1>
    <p class="person-role">General Assistant</p>
  </div>

  <p class="contact contact--lines">
    Tel.: 65 - 63902417<br>
    Fax.: 65 - 63902418<br>
    helena@valtrion.com.sg<br>
    www.valtrion.com.sg
  </p>
</main>
</body>
</html>
```